Auto parts webshop needs a webdesign

We need a webdesign for https://www.volmar.nl/. Brexo delivers parts, Accessories, Rims, Tires, Exhausts for USA cars and old timers. We would like to have a home page to start with. Then, after evaluating, in the second round, we would like a productoverview, productdetail page and a general information page, like about us.
Below some points:
- It's a combination of business to business and business to consumer. So login / registration is necassary | maybe a block on the home page with a button to the a registration page and a text like: registrate to get special discounts and prices
- Shopping cart
- Fixed header
- Mega menu
- Search and filtering (use dummy data)
- Categories: a) based on brands b) based parts
- Colors: color of logo #ff0000 and blue. It doesnt need to be flashy, but somehow professional.
Below 2 sites Brexo likes:
1. https://www.carvinox-depot.nl/
"They have an set up more or less similar to what we want."
2. https://www.qelt-werktuig.com/nl/
"clear and also no nonsense"
Below some designs we already implemented so you can see the functionalities / designgrid:
1. https://fenrip.nl/
2. https://www.molvastay.com/
Parts, Accessories, Rims, Tires, Exhausts for USA cars and old timers
Spare parts cars
4 page
Designer to choose colors to be used in the design.

```html
<!DOCTYPE html>
<html lang="en">
<head>
<meta charset="utf-8">
<title>Brexo – USA Parts &amp; Accessoires</title>
<link href="https://fonts.googleapis.com/css2?family=Lato:ital,wght@0,400;0,700;0,900;1,400&display=swap" rel="stylesheet">
<style>
:root{
  --red:#ff0000;
  --blue:#2a86d8;
  --blue-dark:#1f74c2;
  --ink:#1e1e1e;
  --text:#444;
  --muted:#777;
  --line:#d9d9d9;
  --panel:#f4f4f4;
  --footer:#2b2b2b;
  --copy:#e9e9e9;
}
*{box-sizing:border-box;margin:0;padding:0}
html,body{width:1200px;height:2677px;overflow:hidden}
body{font-family:'Lato',sans-serif;color:var(--text);background:#fff;position:relative}
a{color:inherit;text-decoration:none}
.wrap{width:1052px;margin:0 auto;position:relative}

/* header */
.site-header{height:138px}
.brand{position:absolute;left:0;top:22px}
.brand-name{font-family:'Lato',sans-serif;font-weight:900;font-size:64px;line-height:58px;color:var(--blue);letter-spacing:1px}
.brand-tagline{font-style:italic;font-size:18px;line-height:23px;color:#444;margin-top:6px;letter-spacing:.3px}
.social-top{position:absolute;left:580px;top:28px;display:flex;gap:20px}
.social-dot{width:18px;height:18px;border-radius:50%;background:var(--red)}
.phone{position:absolute;left:808px;top:24px;color:var(--blue);font-size:22px;font-weight:700;display:flex;align-items:center;gap:6px}
.header-icons{position:absolute;left:994px;top:27px;display:flex;gap:16px}
.search{position:absolute;left:447px;top:75px;width:388px;height:44px;border:1px solid #ccc;display:flex;align-items:center;padding:0 14px 0 16px;justify-content:space-between;font-size:13px;color:#555}
.register-btn{position:absolute;left:847px;top:75px;width:205px;height:44px;background:var(--ink);color:#fff;font-weight:900;font-size:16px;display:flex;align-items:center;justify-content:center;letter-spacing:.3px}

.main-nav{height:50px;background:var(--red)}
.main-nav ul{list-style:none;display:flex;justify-content:center;gap:40px;height:50px;align-items:center}
.main-nav li{color:#fff;font-weight:700;font-size:15px;letter-spacing:.2px}

.finder{height:80px;display:flex;justify-content:center;align-items:center;gap:10px;padding-left:2px}
.finder .select{width:159px;height:44px;border:1px solid #ccc;display:flex;align-items:center;justify-content:space-between;padding:0 14px;font-size:13px;color:#444}
.finder .submit{width:159px;height:44px;background:var(--blue);color:#fff;font-weight:900;font-size:16px;display:flex;align-items:center;justify-content:center}

/* hero */
.hero{position:relative;height:630px;background:linear-gradient(180deg,#6aa3d8 0%,#9cc4e6 30%,#8a5c52 55%,#b3171c 72%,#6d6d6d 100%)}
.hero-card{position:absolute;left:711px;top:168px;width:415px;height:295px;background:rgba(25,25,25,.85);padding:20px 29px 0 20px;text-align:right;color:#fff}
.hero-card h1{font-weight:900;font-size:37px;line-height:44px;letter-spacing:.3px}
.hero-card p{font-size:19px;line-height:31px;margin-top:12px;letter-spacing:.2px}
.hero-card .shop-now{display:inline-flex;width:180px;height:48px;background:var(--blue);align-items:center;justify-content:center;font-weight:700;font-size:15px;margin-top:15px}
.dots{position:absolute;left:77px;top:589px;display:flex;gap:11px}
.dots span{width:10px;height:10px;border-radius:50%;background:#555}
.dots span:first-child{background:var(--blue)}

/* categories */
.categories{padding-top:40px}
.section-title{font-weight:700;font-size:22px;color:var(--ink);letter-spacing:.3px}
.categories .section-title{text-align:center}
.cat-row{display:flex;gap:27px;margin-top:29px;position:relative}
.cat-card{width:243px;height:210px;background:var(--panel);text-align:center;padding-top:16px}
.cat-img{width:170px;height:140px;margin:0 auto;border-radius:6px}
.cat-card h3{color:var(--blue);font-weight:400;font-size:20px;margin-top:13px}
.cat-arrow{position:absolute;top:88px}
.cat-arrow.prev{left:-30px}.cat-arrow.next{right:-30px}
.view-all{display:block;width:205px;height:37px;margin:30px auto 0;border:1px solid var(--red);color:var(--red);font-weight:700;font-size:14px;text-align:center;line-height:35px}
.divider{height:1px;background:#999;margin-top:47px}

/* shop */
.shop{display:flex;gap:25px;margin-top:47px}
.sidebar{width:242px}
.side-head{height:47px;background:var(--blue);color:#fff;font-weight:900;font-size:19px;line-height:47px;padding-left:15px}
.side-list{list-style:none;background:var(--panel);padding-bottom:12px}
.side-list li{height:45.3px;border-bottom:1px dashed #bbb;display:flex;align-items:center;padding-left:15px;font-weight:700;font-size:12px;color:#222;gap:13px}
.side-list li:last-child{border-bottom:none}
.side-list li::before{content:"»";color:var(--red);font-size:12px}
.brands{margin-top:20px}
.brands .side-list li{height:46px}

.featured{flex:1}
.featured-head{display:flex;justify-content:space-between;align-items:center;height:50px}
.pager{display:flex;gap:12px}
.pager span{width:31px;height:31px;border:1px solid #ccc;display:flex;align-items:center;justify-content:center}
.grid{display:grid;grid-template-columns:repeat(3,245px);column-gap:25px;row-gap:22px;margin-top:21px}
.product{border:1px solid var(--line);height:318px;text-align:center;padding-top:17px}
.product-img{width:170px;height:145px;margin:0 auto;border-radius:6px}
.product h3{color:var(--blue);font-weight:700;font-size:20px;margin-top:17px;letter-spacing:.2px}
.product p{font-size:16px;line-height:21px;margin-top:7px;color:#555}
.buy{display:flex;justify-content:center;gap:16px;align-items:center;margin-top:22px}
.price{font-size:17px;color:#222;font-weight:400}
.buy-btn{width:120px;height:35px;border:1px solid var(--red);color:var(--red);font-weight:700;font-size:15px;line-height:33px}

/* features */
.features{background:#f5f5f5;height:168px;margin-top:44px;padding-top:46px}
.feature-row{display:flex;gap:25px}
.feature{width:244px;height:70px;border:1px solid var(--red);background:#fff;display:flex;align-items:center;justify-content:center;gap:12px;color:var(--blue);font-size:17px;font-weight:700}

/* footer */
.site-footer{background:var(--footer);height:333px;color:#ddd;padding-top:73px}
.footer-cols{display:flex}
.footer-cols h4{color:#fff;font-weight:700;font-size:17px;letter-spacing:.3px;margin-bottom:8px}
.footer-cols ul{list-style:none;font-size:14px;line-height:31px}
.col-links{width:326px}
.col-links .pair{display:flex;gap:50px}
.col-cat{width:242px}
.col-cat ul{line-height:27px}
.col-acc{width:214px}
.subscribe{width:270px;height:45px;border:1px solid #bbb;display:flex;justify-content:space-between;align-items:center;padding:0 12px 0 16px;font-size:15px;margin-top:12px}
.subscribe b{color:#fff;font-size:17px;font-weight:900}
.follow{margin-top:28px}
.social-foot{display:flex;gap:18px;margin-top:6px}
.social-foot span{width:18px;height:18px;border-radius:50%;background:#fff}
.copyright{background:var(--copy);height:68px;text-align:center;line-height:64px;font-size:12px;color:#333}
</style>
</head>
<body>

<header class="site-header">
  <div class="wrap">
    <div class="brand">
      <div class="brand-name">BREXO</div>
      <div class="brand-tagline">USA Parts &amp; Accessoires, Velgen,<br>Banden, Uitlaten</div>
    </div>
    <div class="social-top" aria-label="Social media">
      <span class="social-dot"></span><span class="social-dot"></span><span class="social-dot"></span>
      <span class="social-dot"></span><span class="social-dot"></span><span class="social-dot"></span>
    </div>
    <div class="phone">
      <svg width="16" height="16" viewBox="0 0 24 24"><path fill="#2a86d8" d="M6.6 10.8a15.1 15.1 0 0 0 6.6 6.6l2.2-2.2c.3-.3.7-.4 1-.2 1.1.4 2.3.6 3.6.6.6 0 1 .4 1 1V20c0 .6-.4 1-1 1A17 17 0 0 1 3 4c0-.6.4-1 1-1h3.5c.6 0 1 .4 1 1 0 1.3.2 2.5.6 3.6.1.3 0 .7-.2 1z"/></svg>
      033-417 2265
    </div>
    <div class="header-icons">
      <svg width="20" height="20" viewBox="0 0 24 24" aria-label="Account"><circle cx="12" cy="7" r="5" fill="#333"/><path d="M2 23c0-6 4-9 10-9s10 3 10 9z" fill="#333"/></svg>
      <svg width="22" height="20" viewBox="0 0 24 22" aria-label="Cart"><path d="M1 8h22l-3 13H4z" fill="#333"/><path d="M6 8l5-7M18 8l-5-7" stroke="#333" stroke-width="2"/><path d="M8 12v6M12 12v6M16 12v6" stroke="#fff" stroke-width="1.6"/></svg>
    </div>
    <div class="search">
      <span>Search..</span>
      <svg width="14" height="14" viewBox="0 0 24 24"><circle cx="10" cy="10" r="7" fill="none" stroke="#111" stroke-width="3"/><path d="M15 15l7 7" stroke="#111" stroke-width="3"/></svg>
    </div>
    <a class="register-btn" href="#">REGISTER NOW</a>
  </div>
</header>

<nav class="main-nav">
  <ul>
    <li>HOME</li><li>ABOUT US</li><li>PRODUCTS</li><li>SHOP BY PARTS</li>
    <li>SHOP BY BARNDS</li><li>NEWS</li><li>SUPPORT</li><li>CONTACT</li>
  </ul>
</nav>

<form class="finder">
  <div class="select">Select Model <svg width="8" height="12" viewBox="0 0 8 12"><path d="M4 0l4 5H0zM4 12L0 7h8z" fill="#333"/></svg></div>
  <div class="select">Select Year <svg width="8" height="12" viewBox="0 0 8 12"><path d="M4 0l4 5H0zM4 12L0 7h8z" fill="#333"/></svg></div>
  <div class="select">Select Product <svg width="8" height="12" viewBox="0 0 8 12"><path d="M4 0l4 5H0zM4 12L0 7h8z" fill="#333"/></svg></div>
  <div class="select">Select Quantity <svg width="8" height="12" viewBox="0 0 8 12"><path d="M4 0l4 5H0zM4 12L0 7h8z" fill="#333"/></svg></div>
  <div class="submit">SUBMIT</div>
</form>

<section class="hero" role="img" aria-label="Classic American cars with open hoods under a blue sky">
  <div class="hero-card">
    <h1>WELCOME TO BREXO<br>PARTS IMPORT!</h1>
    <p>Your supplier of parts &amp; accessories for USA Cars and TrucksDelivery both to wholesalers and to particuliers</p>
    <a class="shop-now" href="#">SHOP NOW</a>
  </div>
  <div class="dots"><span></span><span></span><span></span><span></span></div>
</section>

<section class="categories">
  <div class="wrap">
    <h2 class="section-title">CATEGORIES</h2>
    <div class="cat-row">
      <svg class="cat-arrow prev" width="16" height="26" viewBox="0 0 16 26"><path d="M13 2L3 13l10 11" fill="none" stroke="#555" stroke-width="3"/></svg>
      <div class="cat-card"><div class="cat-img" role="img" aria-label="Chrome alloy rim" style="background:radial-gradient(circle,#e6e6e6 20%,#b5b5b5 60%,#f4f4f4 72%)"></div><h3>Rims</h3></div>
      <div class="cat-card"><div class="cat-img" role="img" aria-label="Stack of tires" style="background:radial-gradient(ellipse,#555 30%,#2a2a2a 60%,#f4f4f4 72%)"></div><h3>Tires</h3></div>
      <div class="cat-card"><div class="cat-img" role="img" aria-label="Rubber floor mats" style="background:radial-gradient(ellipse,#3a3a3a 35%,#222 55%,#f4f4f4 70%)"></div><h3>Accessories</h3></div>
      <div class="cat-card"><div class="cat-img" role="img" aria-label="Chrome exhaust muffler" style="background:radial-gradient(ellipse,#d8d8d8 25%,#a9a9a9 55%,#f4f4f4 70%)"></div><h3>Exhausts</h3></div>
      <svg class="cat-arrow next" width="16" height="26" viewBox="0 0 16 26"><path d="M3 2l10 11L3 24" fill="none" stroke="#555" stroke-width="3"/></svg>
    </div>
    <a class="view-all" href="#">VIEW ALL CATEGORIES</a>
    <div class="divider"></div>

    <div class="shop">
      <aside class="sidebar">
        <div class="side-head">SHOP BY PARTS</div>
        <ul class="side-list">
          <li>NEMO ENIM IPSAM</li><li>VOLUPTATEM QUIA VOLU</li><li>PTAS SIT ASPERNATUR</li><li>AUT ODIT AUT</li>
          <li>VOLUPTATEM QUIA VOLU</li><li>PTAS SIT ASPERNATUR</li><li>AUT ODIT AUT</li><li>PTAS SIT ASPERNATUR</li>
        </ul>
        <div class="brands">
          <div class="side-head">SHOP BY BRANDS</div>
          <ul class="side-list">
            <li>NEMO ENIM IPSAM</li><li>VOLUPTATEM QUIA VOLU</li><li>PTAS SIT ASPERNATUR</li><li>AUT ODIT AUT</li><li>VOLUPTATEM QUIA VOLU</li>
          </ul>
        </div>
      </aside>

      <div class="featured">
        <div class="featured-head">
          <h2 class="section-title">FEATURED PRODUCTS</h2>
          <div class="pager">
            <span><svg width="8" height="12" viewBox="0 0 8 12"><path d="M6 1L1 6l5 5" fill="none" stroke="#333" stroke-width="1.5"/></svg></span>
            <span><svg width="8" height="12" viewBox="0 0 8 12"><path d="M2 1l5 5-5 5" fill="none" stroke="#333" stroke-width="1.5"/></svg></span>
          </div>
        </div>
        <div class="grid">
          <article class="product"><div class="product-img" role="img" aria-label="Polished steel wheel" style="background:radial-gradient(circle,#eee 25%,#bdbdbd 58%,#fff 72%)"></div><h3>PRODUCT HEADING</h3><p>Excepteur sint occaecat cup<br>datat non proident</p><div class="buy"><span class="price">$ 509.00</span><a class="buy-btn" href="#">BUY NOW</a></div></article>
          <article class="product"><div class="product-img" role="img" aria-label="Car battery" style="background:radial-gradient(ellipse,#2d5fa8 20%,#222 50%,#fff 70%)"></div><h3>PRODUCT HEADING</h3><p>Excepteur sint occaecat cup<br>datat non proident</p><div class="buy"><span class="price">$ 509.00</span><a class="buy-btn" href="#">BUY NOW</a></div></article>
          <article class="product"><div class="product-img" role="img" aria-label="Tire on alloy wheel" style="background:radial-gradient(ellipse,#cfcfcf 18%,#222 45%,#fff 68%)"></div><h3>PRODUCT HEADING</h3><p>Excepteur sint occaecat cup<br>datat non proident</p><div class="buy"><span class="price">$ 509.00</span><a class="buy-btn" href="#">BUY NOW</a></div></article>
          <article class="product"><div class="product-img" role="img" aria-label="Ignition distributor with red cap" style="background:radial-gradient(ellipse,#d42a2a 15%,#8a8a8a 38%,#fff 60%)"></div><h3>PRODUCT HEADING</h3><p>Excepteur sint occaecat cup<br>datat non proident</p><div class="buy"><span class="price">$ 509.00</span><a class="buy-btn" href="#">BUY NOW</a></div></article>
          <article class="product"><div class="product-img" role="img" aria-label="Brake pads" style="background:radial-gradient(ellipse,#5a5a5a 25%,#3b3b3b 45%,#fff 65%)"></div><h3>PRODUCT HEADING</h3><p>Excepteur sint occaecat cup<br>datat non proident</p><div class="buy"><span class="price">$ 509.00</span><a class="buy-btn" href="#">BUY NOW</a></div></article>
          <article class="product"><div class="product-img" role="img" aria-label="Clutch kit" style="background:radial-gradient(ellipse,#666 20%,#bbb 48%,#fff 68%)"></div><h3>PRODUCT HEADING</h3><p>Excepteur sint occaecat cup<br>datat non proident</p><div class="buy"><span class="price">$ 509.00</span><a class="buy-btn" href="#">BUY NOW</a></div></article>
        </div>
      </div>
    </div>
  </div>
</section>

<section class="features">
  <div class="wrap feature-row">
    <div class="feature"><svg width="36" height="28" viewBox="0 0 36 28"><rect x="0" y="3" width="21" height="17" rx="2" fill="#f00"/><path d="M21 8h8l6 7v5H21z" fill="#f00"/><circle cx="8" cy="22" r="4.5" fill="#f00" stroke="#fff" stroke-width="2"/><circle cx="28" cy="22" r="4.5" fill="#f00" stroke="#fff" stroke-width="2"/></svg>DIRECT&nbsp; DELIVERY</div>
    <div class="feature"><svg width="36" height="26" viewBox="0 0 36 26"><rect x="6" y="2" width="24" height="16" rx="1" fill="none" stroke="#f00" stroke-width="2.5"/><path d="M1 21h34l-2 4H3z" fill="#f00"/></svg>ORDER ONLINE</div>
    <div class="feature"><svg width="32" height="32" viewBox="0 0 32 32"><circle cx="16" cy="16" r="13" fill="none" stroke="#f00" stroke-width="3.5"/><path d="M16 8v9h-6" fill="none" stroke="#f00" stroke-width="3"/></svg>BUSINESS HOURS</div>
    <div class="feature"><svg width="32" height="32" viewBox="0 0 32 32"><path d="M3 27L17 13" stroke="#f00" stroke-width="6" stroke-linecap="round"/><circle cx="22" cy="9" r="8" fill="#f00"/><circle cx="25" cy="6" r="3.5" fill="#fff"/></svg>AFTER SALE SERVICE</div>
  </div>
</section>

<footer class="site-footer">
  <div class="wrap footer-cols">
    <div class="col-links">
      <h4>QUICK LINKS</h4>
      <div class="pair">
        <ul><li>Home</li><li>About Us</li><li>Products</li><li>Shop By Parts</li><li>News</li></ul>
        <ul style="margin-top:-4px"><li>Shop By Barnds</li><li>Support</li><li>Contact</li></ul>
      </div>
    </div>
    <div class="col-cat">
      <h4>CATEGORIES</h4>
      <ul><li>Excepteur sint</li><li>occaecat cupidatat non</li><li>Proident sunt</li><li>Culpa qui officia</li><li>Deserunt mollit anim</li><li>Est laborum</li></ul>
    </div>
    <div class="col-acc">
      <h4>MY ACCOUNT</h4>
      <ul><li>Log In</li><li>My Account</li><li>Register</li><li>Return Policy</li><li>Wishlist</li></ul>
    </div>
    <div>
      <h4>EMAIL SUBSCRIBE</h4>
      <div class="subscribe"><span>Enter Email Address</span><b>GO</b></div>
      <h4 class="follow">FOLLOW US</h4>
      <div class="social-foot"><span></span><span></span><span></span><span></span><span></span><span></span></div>
    </div>
  </div>
</footer>
<div class="copyright">Copyright © 2022 &nbsp;Company Name. All Right Reserved</div>

</body>
</html>
```